Business cards real estate company

We need a design for a business card. It is a company that specializes in real estate sales. There should be space for a photo of the respective employee as well as the website and telephone number on it. Design should be noble, innovative.

Contact Information for Business Card

Website, Name, Position, Telefonnummer

Requirements
Must have
• Photo, logo

```html
<!DOCTYPE html>
<html lang="en">
<head>
<meta charset="utf-8">
<title>Casavera Business Card</title>
<link rel="stylesheet" href="https://fonts.googleapis.com/css2?family=Montserrat:wght@400;500;600;700&display=swap">
<style>
  :root {
    --bg: #d9d9d7;
    --card-white: #ffffff;
    --brand-green: #7ab842;
    --brand-green-dark: #5f9a30;
    --name-green: #6aae3a;
    --text-grey: #4a4a4a;
    --photo-light: #f2f5f9;
    --photo-blue: #a9c3e6;
  }
  * { margin: 0; padding: 0; box-sizing: border-box; }
  html, body {
    width: 1200px; height: 801px; overflow: hidden;
    background: var(--bg);
    font-family: "Montserrat", sans-serif;
  }
  .stage {
    width: 1200px; height: 801px;
    display: flex; align-items: center; justify-content: center; gap: 60px;
  }
  .card {
    width: 500px; height: 286px;
    border-radius: 16px;
    position: relative; overflow: hidden;
    box-shadow: 0 6px 18px rgba(0,0,0,0.18);
  }
  .card--front { background: var(--card-white); }
  .card--back {
    background: var(--brand-green);
    display: flex; align-items: center; justify-content: center;
  }
  .portrait {
    position: absolute; right: 0; top: 0;
    width: 210px; height: 286px;
    background: linear-gradient(180deg, var(--photo-light) 0%, var(--photo-light) 30%, var(--photo-blue) 100%);
  }
  .edge-tab {
    position: absolute; left: 0; bottom: 56px;
    width: 6px; height: 22px;
    background: var(--brand-green);
    border-radius: 0 3px 3px 0;
  }
  .details { position: absolute; left: 34px; top: 46px; }
  .brand-name {
    font-weight: 600; font-size: 40px; letter-spacing: 0.5px;
    color: var(--brand-green); line-height: 1;
  }
  .person-name {
    margin-top: 18px;
    font-weight: 700; font-size: 17px; color: var(--name-green);
  }
  .person-role { font-size: 13px; color: var(--text-grey); margin-top: 2px; }
  .address {
    margin-top: 14px; font-size: 12.5px; color: var(--text-grey); line-height: 1.4;
  }
  .contacts { margin-top: 12px; list-style: none; }
  .contacts li {
    display: flex; align-items: center; gap: 8px;
    font-size: 12.5px; color: var(--text-grey); line-height: 1.55;
  }
  .contacts svg { width: 11px; height: 11px; flex: none; }
  .brand-name--back {
    font-weight: 600; font-size: 62px; color: var(--card-white); letter-spacing: 1px;
  }
</style>
</head>
<body>
<main class="stage">
  <section class="card card--front">
    <div class="portrait" role="img" aria-label="Portrait photo of the employee in a light blue shirt and tie"></div>
    <span class="edge-tab"></span>
    <div class="details">
      <div class="brand-name">Casavera</div>
      <div class="person-name">Daniel Marlow</div>
      <div class="person-role">President</div>
      <div class="address">1820 Harbor View Lane<br>Seacliff CA 90412</div>
      <ul class="contacts">
        <li>
          <svg viewBox="0 0 12 12"><path fill="#7ab842" d="M2.5 1l2 2-1 1.3a7 7 0 0 0 4.2 4.2L9 7.5l2 2-1.3 1.5C5.5 11 1 6.5 1 2.3z"/></svg>
          555-014-2290
        </li>
        <li>
          <svg viewBox="0 0 12 12"><rect x="1" y="2.5" width="10" height="7" rx="1" fill="#7ab842"/><path d="M1.5 3l4.5 3.5L10.5 3" stroke="#fff" stroke-width="1" fill="none"/></svg>
          hello@casavera.com
        </li>
        <li>
          <svg viewBox="0 0 12 12"><circle cx="6" cy="6" r="5" fill="none" stroke="#7ab842" stroke-width="1.4"/><path d="M1 6h10M6 1c2 2 2 8 0 10M6 1c-2 2-2 8 0 10" stroke="#7ab842" stroke-width="1" fill="none"/></svg>
          www.casavera.com
        </li>
      </ul>
    </div>
  </section>
  <section class="card card--back">
    <div class="brand-name--back">Casavera</div>
  </section>
</main>
</body>
</html>
```